4 Banners for homepage and logo

Logo for SiteTitleCounsel.net and 4 banners for the center of the page.

Logo should be clean and pretty basic.

Banners
1.
Domain Name Disputes
We'll recover your domain names, Guaranteed or its free!

2.
Reputation management
We get defamatory content removed from Quorvix, Brindle, Chatterloom, and Pallbook!

3.
Domain name management
Create an offensive or defensive domain name strategy for your company

4.
Defensive reputation management
Get ahead of the game and make your image shine online!

```html
<!DOCTYPE html>
<html lang="en">
<head>
<meta charset="utf-8">
<title>SiteTitleCounsel.net — Logo and Banners</title>
<link rel="stylesheet" href="https://fonts.googleapis.com/css2?family=Barlow:wght@400;600;700;800;900&display=swap">
<style>
  :root {
    --ink: #000000;
    --paper: #ffffff;
    --sun: #ffee11;
    --sun-soft: #ffe866;
    --flag-red: #ee0000;
    --royal-violet: #6a22ee;
    --lavender: #b8b8ff;
    --ember: #ff4422;
    --sand: #d9c190;
    --magenta: #ff11ee;
  }
  html, body {
    margin: 0;
    padding: 0;
    width: 900px;
    height: 1200px;
    overflow: hidden;
    background: var(--paper);
  }
  .canvas {
    position: relative;
    width: 900px;
    height: 1200px;
  }
  .art {
    position: absolute;
    inset: 0;
    width: 900px;
    height: 1200px;
  }
  .art text { font-family: "Barlow", Arial, sans-serif; }
  .outline { stroke: var(--ink); stroke-width: 3; stroke-linejoin: miter; }
  .shadow { fill: var(--ink); }
  .bold { font-weight: 800; }
  .light { font-weight: 400; }
  .headline { font-size: 44px; }
  .tagline { font-size: 19px; font-weight: 800; fill: var(--ink); }
  .callout { font-weight: 900; fill: var(--ink); }
</style>
</head>
<body>
<div class="canvas">
  <svg class="art" viewBox="0 0 900 1200" xmlns="http://www.w3.org/2000/svg">

    <!-- Logo -->
    <g class="logo">
      <polygon class="shadow" points="92,54 700,80 678,142 62,158"/>
      <polygon class="outline" fill="var(--sun)" points="82,42 690,68 668,130 52,145"/>
      <text x="95" y="107" class="headline" fill="var(--ink)"><tspan class="bold">Site</tspan><tspan class="light">Title</tspan><tspan class="bold">Counsel</tspan><tspan class="light">.net</tspan></text>
    </g>

    <!-- Banner: domain name disputes -->
    <g class="banner banner-disputes">
      <polygon class="shadow" points="612,268 776,258 806,418 360,356 510,300"/>
      <polygon class="outline" fill="var(--sun)" points="612,262 776,258 806,418 360,352 510,300"/>
      <polygon class="shadow" points="72,214 622,234 610,294 72,314"/>
      <polygon class="outline" fill="var(--flag-red)" points="88,205 612,226 600,286 62,305"/>
      <text x="98" y="272" class="headline" fill="var(--sun)"><tspan class="bold">Domain</tspan><tspan class="light" fill="var(--paper)">Name</tspan><tspan class="bold">Disputes</tspan><tspan class="bold" fill="var(--paper)">?</tspan></text>
      <polygon class="outline" fill="var(--paper)" points="96,316 508,306 505,354 108,368"/>
      <text x="124" y="342" class="tagline">We’ll recover your domain names,</text>
      <text x="526" y="338" class="callout" font-size="38">Guaranteed</text>
      <text x="548" y="380" class="callout" font-size="38"><tspan font-weight="400">or it’s </tspan><tspan>free!</tspan></text>
      <polygon fill="var(--flag-red)" points="676,386 780,388 778,401"/>
    </g>

    <!-- Banner: reputation management -->
    <g class="banner banner-reputation">
      <polygon class="shadow" points="604,512 838,497 866,660 330,616 594,562"/>
      <polygon class="outline" fill="var(--lavender)" points="600,505 838,492 866,656 330,612 590,555"/>
      <polygon class="shadow" points="90,468 618,490 606,550 62,566"/>
      <polygon class="outline" fill="var(--royal-violet)" points="80,458 608,482 598,540 55,558"/>
      <text x="90" y="524" class="headline" fill="var(--sun)"><tspan class="bold">Reputation</tspan><tspan class="light" fill="var(--paper)">Management</tspan></text>
      <polygon class="outline" fill="var(--sun-soft)" points="78,566 592,556 582,606 84,622"/>
      <text x="97" y="596" class="tagline" font-size="18">We get defamatory content removed from:-</text>
      <text x="745" y="540" class="callout" font-size="32" font-weight="800" text-anchor="end">Quorvix,</text>
      <text x="826" y="578" class="callout" font-size="32" font-weight="800" text-anchor="end">Brindle, Chatterloom</text>
      <text x="830" y="615" class="callout" font-size="32" font-weight="800" text-anchor="end">and Pallbook!</text>
    </g>

    <!-- Banner: domain name management -->
    <g class="banner banner-domain-management">
      <polygon class="shadow" points="136,778 782,730 862,894 154,860"/>
      <polygon class="outline" fill="var(--sand)" points="128,770 778,722 858,888 150,852"/>
      <polygon class="shadow" points="90,678 672,700 660,760 70,778"/>
      <polygon class="outline" fill="var(--ember)" points="80,668 662,690 650,750 62,770"/>
      <text x="98" y="736" class="headline" fill="var(--sun)"><tspan class="bold">Domain</tspan><tspan class="light" fill="var(--paper)">Name</tspan><tspan class="bold">Managment</tspan></text>
      <text x="170" y="814" class="callout" font-size="35"><tspan font-weight="800">Create an </tspan><tspan font-weight="400">offensive </tspan><tspan font-weight="800">or </tspan><tspan font-weight="400">defensive</tspan></text>
      <text x="192" y="848" class="callout" font-size="27" font-weight="800">domain name strategy for your company.</text>
    </g>

    <!-- Banner: defensive reputation management -->
    <g class="banner banner-defensive">
      <polygon class="shadow" points="102,1030 816,1002 788,1130 122,1148"/>
      <polygon class="outline" fill="var(--sun)" points="95,1020 810,995 780,1120 118,1138"/>
      <polygon class="shadow" points="60,928 798,950 786,1010 30,1022"/>
      <polygon class="outline" fill="var(--magenta)" points="52,918 788,942 776,1000 22,1012"/>
      <text x="58" y="983" class="headline" fill="var(--sun)"><tspan class="bold">Defensive</tspan><tspan class="light" fill="var(--ink)">Reputation</tspan><tspan class="bold">Management</tspan></text>
      <text x="128" y="1056" class="callout" font-size="37" font-weight="400">Get ahead of the game and make</text>
      <text x="150" y="1106" class="callout" font-size="48">your image shine online!</text>
    </g>
  </svg>
</div>
</body>
</html>
```